Wine Label for new family wine label

we need a new wine label and name for our new group winemaking project. There are 10 of us in the group, plus two wine growers and two winemakers. We will be making wines on an ongoing basis but relatively small scale. The wines will be coming from the barossa valley and coonawarra. They will be high end wines - built on great dirt, some great history with the growers, and ultimately great grapes. We will be initially producing 4 wines, a shiraz, a cab, and a blend plus one high end single block shiraz based wine.

We are looking for the wine label to reflect quality, family and friendship.

Reason: will provide a better brief

Graphic Design

```html
<!DOCTYPE html>
<html lang="en">
<head>
<meta charset="utf-8">
<title>Cedar Row Shiraz 2014 Label</title>
<link rel="stylesheet" href="https://fonts.googleapis.com/css2?family=Cormorant+Garamond:wght@400;500&family=Pinyon+Script&display=swap">
<style>
  :root {
    --backdrop: #f6eee3;
    --label: #1c1c1c;
    --label-edge: #2a2a2a;
    --frame: #6f6f6f;
    --ink: #d9d9d9;
    --ink-soft: #a9a9a9;
  }
  html, body {
    margin: 0;
    padding: 0;
    overflow: hidden;
  }
  body {
    width: 733px;
    height: 1200px;
    background: var(--backdrop);
    position: relative;
  }
  .label {
    position: absolute;
    left: 166px;
    top: 120px;
    width: 400px;
    height: 960px;
    background: var(--label);
    box-shadow: inset 0 0 0 2px var(--label-edge);
    color: var(--ink);
    text-align: center;
  }
  .label__frame {
    position: absolute;
    inset: 12px;
    border: 1.5px solid var(--frame);
  }
  .label__block {
    position: absolute;
    left: 0;
    right: 0;
    margin: 0;
  }
  .vintage, .variety {
    font-family: "Cormorant Garamond", serif;
    font-weight: 500;
    font-size: 36px;
    line-height: 1;
  }
  .vintage { top: 62px; }
  .variety { top: 108px; }
  .wine-name {
    top: 190px;
    font-family: "Cormorant Garamond", serif;
    font-weight: 400;
    font-size: 62px;
    letter-spacing: 1px;
    line-height: 1;
  }
  .region {
    top: 282px;
    font-family: "Pinyon Script", cursive;
    font-size: 24px;
    color: var(--ink-soft);
  }
  .divider {
    left: 70px;
    right: 70px;
    width: 260px;
    margin: 0 auto;
  }
  .divider--top { top: 328px; }
  .divider--bottom { top: 752px; }
  .story {
    top: 352px;
    padding: 0 48px;
    font-family: "Pinyon Script", cursive;
    font-size: 19px;
    line-height: 34px;
    color: var(--ink-soft);
  }
  .members {
    top: 500px;
    list-style: none;
    padding: 0;
    font-family: "Pinyon Script", cursive;
    font-size: 23px;
    line-height: 54px;
    color: var(--ink-soft);
  }
  .maker-name {
    top: 820px;
    font-family: "Cormorant Garamond", serif;
    font-weight: 400;
    font-size: 24px;
    letter-spacing: 3px;
    color: var(--ink-soft);
  }
</style>
</head>
<body>
  <section class="label" aria-label="Cedar Row Shiraz 2014 wine label">
    <div class="label__frame"></div>

    <p class="label__block vintage">2014</p>
    <p class="label__block variety">Shiraz</p>
    <h1 class="label__block wine-name">CEDAR ROW</h1>
    <p class="label__block region">Barossa Valley and Coonawarra</p>

    <svg class="label__block divider divider--top" viewBox="0 0 260 10" height="10" aria-hidden="true">
      <line x1="0" y1="2" x2="260" y2="2" stroke="#8a8a8a" stroke-width="1"/>
      <polygon points="125,2 135,2 130,9" fill="#bdbdbd"/>
    </svg>

    <p class="label__block story">
      A wine of old vines, grown on rich red earth,<br>
      shared by good friends over many seasons,<br>
      made with the heart of our whole family.
    </p>

    <ul class="label__block members">
      <li>Name 1 · Name 2</li>
      <li>Name 3 · Name 4</li>
      <li>Name 5 · Name 6</li>
      <li>Name 7 · Name 8</li>
      <li>Name 9 · Name 10</li>
    </ul>

    <svg class="label__block divider divider--bottom" viewBox="0 0 260 10" height="10" aria-hidden="true">
      <line x1="0" y1="8" x2="260" y2="8" stroke="#8a8a8a" stroke-width="1"/>
      <polygon points="125,8 135,8 130,1" fill="#bdbdbd"/>
    </svg>

    <p class="label__block maker-name">CEDAR ROW</p>
  </section>
</body>
</html>
```